Hvac and insulation company needs good looking business card design

We are hvac and insulation company and looking for a new business cards that look to today standards designs

Target Market(s)

homeowners

Industry/Entity Type

Hvac

Contact Information for Business Card

Name: Doran Velkisk
Home comfort consultant
address: 4827 Brimwood Ct #215 Oakland, CA 94619
office: 888-731-5096
cell: 510-874-3190
Lic.# 648215
Email: doran@quorvix-hvac.example
Web: quorvix-hvac.example

Requirements
Must have
• clean and sleek look
Nice to have
• simple with a clean look
Should not have
• to busy business card

```html
<!DOCTYPE html>
<html lang="en">
<head>
<meta charset="utf-8">
<title>Quorvix Business Card</title>
<link rel="stylesheet" href="https://fonts.googleapis.com/css2?family=Arimo:wght@400;700&display=swap">
<style>
  :root {
    --stage: #3a3a3a;
    --card-light: #ececec;
    --brand-orange: #f3851f;
    --brand-grey: #7e7e7f;
    --ink: #1e1e1e;
    --rule: #8a8a8a;
    --white: #ffffff;
  }
  * { box-sizing: border-box; margin: 0; padding: 0; }
  html, body {
    width: 1200px; height: 900px; overflow: hidden;
    background: var(--stage);
    font-family: "Arimo", Arial, sans-serif;
  }
  .card {
    position: absolute; top: 170px;
    width: 347px; height: 561px;
    overflow: hidden;
  }
  .card--front { left: 259px; background: var(--card-light); }
  .card--back { left: 631px; background: var(--brand-grey); }

  .brand {
    position: absolute; top: 126px; left: 0; right: 0; height: 48px;
    display: flex; align-items: center; justify-content: center; gap: 12px;
  }
  .brand__dot {
    width: 40px; height: 40px; border-radius: 50%;
    background: var(--brand-orange);
  }
  .brand__name {
    font-size: 44px; font-weight: 400; color: var(--brand-orange);
    letter-spacing: 0.5px; line-height: 1;
  }

  .person { position: absolute; top: 272px; left: 0; right: 0; text-align: center; }
  .person__name {
    font-size: 19px; font-weight: 700; color: var(--brand-orange);
    letter-spacing: 0.3px; line-height: 22px;
  }
  .person__role { font-size: 16px; color: var(--ink); line-height: 24px; }

  .icon-row {
    position: absolute; top: 330px; left: 72px; width: 202px;
    display: flex; align-items: center; gap: 3px;
  }
  .icon-row__rule { flex: 1; height: 1px; background: var(--rule); }
  .icon-row__icons { display: flex; gap: 3px; padding: 0 3px; }
  .icon {
    width: 22px; height: 22px; border-radius: 50%;
    background: var(--brand-orange);
    display: flex; align-items: center; justify-content: center;
  }
  .icon svg { width: 12px; height: 12px; }

  .contact {
    position: absolute; top: 356px; left: 0; right: 0;
    text-align: center; font-size: 15px; line-height: 20px; color: var(--ink);
  }
  .divider {
    position: absolute; top: 447px; left: 72px; width: 202px;
    height: 1px; background: var(--rule);
  }
  .address {
    position: absolute; top: 458px; left: 0; right: 0;
    text-align: center; font-size: 15px; line-height: 20px; color: var(--ink);
  }
  .license-band {
    position: absolute; bottom: 0; left: 0; right: 0; height: 50px;
    background: var(--brand-orange); color: var(--white);
    font-size: 15px; display: flex; align-items: center; justify-content: center;
  }

  .back__top {
    position: absolute; top: 0; left: 0; right: 0; height: 415px;
    background: var(--brand-orange);
  }
  .back__name {
    position: absolute; top: 250px; left: 0; right: 0;
    text-align: center; font-size: 56px; color: var(--white); line-height: 1;
  }
  .back__web {
    position: absolute; top: 498px; left: 0; right: 0;
    text-align: center; font-size: 15px; color: var(--white); letter-spacing: 0.3px;
  }
</style>
</head>
<body>
  <section class="card card--front" aria-label="Card front">
    <div class="brand">
      <span class="brand__dot"></span>
      <span class="brand__name">quorvix</span>
    </div>

    <div class="person">
      <p class="person__name">DORAN VELKISK</p>
      <p class="person__role">Home Comfort Consultant</p>
    </div>

    <div class="icon-row">
      <span class="icon-row__rule"></span>
      <div class="icon-row__icons">
        <span class="icon" aria-label="Office phone">
          <svg viewBox="0 0 12 12"><path d="M1 5 Q6 1 11 5 L10 6.5 8.5 5.5 8.5 4.5 Q6 3.6 3.5 4.5 L3.5 5.5 2 6.5 Z M3 7 H9 L10 11 H2 Z" fill="#fff"/></svg>
        </span>
        <span class="icon" aria-label="Mobile phone">
          <svg viewBox="0 0 12 12"><rect x="3" y="0.5" width="6" height="11" rx="1" fill="none" stroke="#fff" stroke-width="1.2"/><circle cx="6" cy="9.5" r="0.7" fill="#fff"/></svg>
        </span>
        <span class="icon" aria-label="Email">
          <svg viewBox="0 0 12 12"><rect x="1" y="2.5" width="10" height="7" fill="#fff"/><path d="M1 2.5 L6 6.5 L11 2.5" fill="none" stroke="#f3851f" stroke-width="1"/></svg>
        </span>
        <span class="icon" aria-label="Website">
          <svg viewBox="0 0 12 12"><circle cx="6" cy="6" r="5" fill="none" stroke="#fff" stroke-width="1.1"/><ellipse cx="6" cy="6" rx="2.2" ry="5" fill="none" stroke="#fff" stroke-width="0.9"/><path d="M1 6 H11" stroke="#fff" stroke-width="0.9"/></svg>
        </span>
      </div>
      <span class="icon-row__rule"></span>
    </div>

    <div class="contact">
      <p>888-731-5096</p>
      <p>510-874-3190</p>
      <p>doran@quorvix-hvac.example</p>
      <p>www.quorvix-hvac.example</p>
    </div>

    <div class="divider"></div>

    <div class="address">
      <p>4827 Brimwood Ct</p>
      <p>#215 Oakland, CA 94619</p>
    </div>

    <div class="license-band">LIC.# 648215</div>
  </section>

  <section class="card card--back" aria-label="Card back">
    <div class="back__top"></div>
    <p class="back__name">quorvix</p>
    <p class="back__web">www.quorvix-hvac.example</p>
  </section>
</body>
</html>
```